Anzeigengestaltung für Stellenanzeige
Zielgruppe
Wir sind ein Abrechnungsunternehmen das für Zahnärzte die zahnmedizinische und zahntechnische Abrechnung von extern übernimmt.
Aufgrund einer Erweiterung suchen wir neues Personal welches uns unterstützt. Deshalb benötigen wir einen Stellenanzeige.
Wir suchen Personal - zahnmedizinische Fachangestellte mit Erfahrung in der Abrechnung
Abkürzungen: ZFA oder ZMV beides gewünscht wenn Abrechnungskenntnisse vorhanden sind.
Aufgabenstellung
Bitte Stellenanzeige unserer Website anpassen, www.zahnkanzleimerwen.de
logo bitte con Website übernehmen.
Moderne Gestaltung
Wir bieten:
-Anstellung Teilzeit oder Vollzeit
-Ein motiviertes und kompetentes Team
-Fort- und Weitermöglichkeiten
-Flexible Arbeits- und Urlaubszeiten
-Attraktive leistungsgerechte Bezahlung
Ihr Profil
Um die Stelle gut ausfüllen zu können, wünschen wir uns von Ihnen:
Abgeschlossene Ausbildung zum/zur Zahnmedizinische Fachangestellte, Zahnmedizinische Verwaltungsfachangestellte (m/w/d)
Selbstständiges Arbeiten und Einsatzbereitschaft
Gute PC-Kenntnisse und sicherer Umgang mit gängigen Office-Anwendungen
Erfahrung in der zahmedizinischen Abrechnung
Sorgfalt, Teamfähigkeit
Engagement und Freude am Beruf
Wir haben Ihr Interesse geweckt dann senden Sie uns Ihre Bewerbung an: t.brellmann@zahnkanzleimerwen.de
------Beispiel----------
Gerne auch eigene Beispiele....

```html
<!DOCTYPE html>
<html lang="de">
<head>
<meta charset="utf-8">
<title>Stellenanzeige – Zahnkanzlei Merwen</title>
<link rel="stylesheet" href="https://fonts.googleapis.com/css2?family=Jost:wght@300;400;500;600&display=swap">
<style>
  :root {
    --stone-light: #9d9990;
    --stone-dark: #8c887f;
    --ink: #26251f;
    --paper: #ffffff;
    --night: #161616;
    --night-soft: #232323;
    --sand: #cfc6b8;
    --photo-top: #3a3431;
    --photo-mid: #b49f86;
    --photo-low: #2a2624;
  }
  * { margin: 0; padding: 0; box-sizing: border-box; }
  html, body { width: 858px; height: 1200px; overflow: hidden; }
  body { font-family: "Jost", "Futura", sans-serif; }
  .ad {
    position: relative; width: 858px; height: 1200px; overflow: hidden;
    background: linear-gradient(160deg, var(--stone-light) 0%, var(--stone-dark) 100%);
    color: var(--paper);
  }
  .line {
    position: absolute; left: 0; width: 100%; text-align: center;
    font-weight: 300; font-size: 21px; line-height: 1; letter-spacing: 0.1px;
    white-space: nowrap;
  }
  .title {
    position: absolute; left: 0; width: 100%; top: 71px; text-align: center;
    font-weight: 500; font-size: 33px; letter-spacing: 0.5px; color: var(--ink);
  }
  .section-head {
    position: absolute; left: 0; width: 100%; text-align: center;
    font-weight: 500; font-size: 22px; color: var(--ink);
  }
  .brand {
    position: absolute; left: 516px; top: 812px; width: 280px; text-align: center;
  }
  .brand-mark {
    display: inline-block; width: 14px; height: 14px; border-radius: 50%;
    background: var(--paper); margin-right: 8px; vertical-align: middle;
  }
  .brand-name {
    font-weight: 500; font-size: 28px; color: var(--paper); vertical-align: middle;
  }
  .brand-tag {
    display: block; margin-top: 10px; font-weight: 500; font-size: 10.5px;
    letter-spacing: 1.6px; color: var(--paper);
  }
  .contact-band {
    position: absolute; left: 0; top: 941px; width: 858px; height: 259px;
    background: linear-gradient(180deg, var(--night-soft), var(--night));
  }
  .contact-head {
    position: absolute; left: 60px; width: 414px; top: 62px; text-align: center;
    font-weight: 500; font-size: 22px; line-height: 29px; color: var(--sand);
  }
  .contact-text {
    position: absolute; left: 60px; width: 414px; top: 150px; text-align: center;
    font-weight: 300; font-size: 21px; color: var(--paper);
  }
  .contact-mail {
    position: absolute; left: 40px; width: 454px; top: 177px; text-align: center;
    font-weight: 600; font-size: 20px; color: var(--paper);
  }
  .team-photo {
    position: absolute; left: 540px; top: 30px; width: 270px; height: 229px;
    border-radius: 120px 120px 0 0;
    background: radial-gradient(ellipse at 50% 70%, var(--photo-mid) 0%, var(--photo-top) 55%, var(--night) 100%);
    opacity: 0.85;
  }
</style>
</head>
<body>
<main class="ad">
  <h1 class="title">WIR SUCHEN PERSONAL!</h1>

  <p class="line" style="top:156px">Zahnmedizinische Fachangestellte mit Erfahrung in der Abrechnung</p>
  <p class="line" style="top:186px">Abkürzung: ZFA oder ZMV beides gewünscht, wenn</p>
  <p class="line" style="top:217px">Abrechnungskenntnisse vorhanden sind</p>

  <h2 class="section-head" style="top:273px">WIR BIETEN:</h2>
  <p class="line" style="top:307px">• Anstellung Teilzeit oder Vollzeit</p>
  <p class="line" style="top:337px">• Ein motiviertes und kompetentes Team</p>
  <p class="line" style="top:367px">• Fort- und Weitermöglichkeiten</p>
  <p class="line" style="top:398px">• Flexible Arbeits- und Urlaubszeiten</p>
  <p class="line" style="top:428px">• Attraktive leistungsgerechte Bezahlung</p>

  <h2 class="section-head" style="top:485px">IHR PROFIL:</h2>
  <p class="line" style="top:519px">Um die Stelle gut ausfüllen zu können, wünschen wir uns von Ihnen:</p>
  <p class="line" style="top:549px">• Abgeschlossene Ausbildung zum/zur Zahnmedizinische Fachangestellte,</p>
  <p class="line" style="top:580px">Zahnmedizinische Verwaltungsfachangestellte (m/w/d)</p>
  <p class="line" style="top:610px">• Selbstständiges Arbeiten und Einsatzbereitschaft</p>
  <p class="line" style="top:640px">• Gute PC-Kenntnisse und sicherer Umgang mit gängigen</p>
  <p class="line" style="top:671px">Office-Anwendungen</p>
  <p class="line" style="top:701px">• Erfahrung in der zahmedizinischen Abrechnung</p>
  <p class="line" style="top:731px">• Sorgfalt, Teamfähigkeit</p>
  <p class="line" style="top:762px">• Engagement und Freude am Beruf</p>

  <div class="brand">
    <span class="brand-mark"></span><span class="brand-name">Zahnkanzlei Merwen</span>
    <span class="brand-tag">Zahnärztliche Abrechnung &amp; Management</span>
  </div>

  <section class="contact-band">
    <h2 class="contact-head">WIR HABEN IHR INTERESSE<br>GEWECKT?!</h2>
    <p class="contact-text">Dann senden Sie uns Ihre Bewerbung an:</p>
    <p class="contact-mail">t.brellmann@zahnkanzleimerwen.de</p>
    <div class="team-photo" role="img" aria-label="Foto von zwei Mitarbeiterinnen des Teams in beigen Blazern"></div>
  </section>
</main>
</body>
</html>
```